Construction business card

I need a new business card, they can connect with my logo, brand.
What we do is residential house , design and build
I like: Navy blue / black
I attached our logo, brand,
and, some idea for business card.

```html
<!DOCTYPE html>
<html lang="en">
<head>
<meta charset="UTF-8">
<title>Ridgeline Building Group – Business Card</title>
<link href="https://fonts.googleapis.com/css2?family=Poppins:wght@400;500;600;700&display=swap" rel="stylesheet">
<style>
  :root {
    --page-bg: #17191c;
    --card-bg: #25292e;
    --card-edge: #2e3339;
    --brand-blue: #1f7fd6;
    --text-white: #f3f5f7;
    --text-soft: #d9dde2;
    --silver: #8d939a;
  }
  * { box-sizing: border-box; margin: 0; padding: 0; }
  html, body {
    width: 1200px; height: 800px; overflow: hidden;
    background: var(--page-bg);
    font-family: "Poppins", sans-serif;
  }
  .canvas {
    position: relative; width: 1200px; height: 800px;
    display: flex; align-items: center; justify-content: center; gap: 40px;
  }
  .card {
    position: relative; width: 540px; height: 310px;
    background: var(--card-bg);
    border: 1px solid var(--card-edge);
    border-radius: 22px;
    overflow: hidden;
  }

  /* Front */
  .card-front { display: flex; align-items: center; justify-content: center; }
  .front-brand {
    color: var(--silver); font-weight: 700; font-size: 30px;
    letter-spacing: 1px; text-transform: uppercase; text-align: center; line-height: 1.15;
  }

  /* Back */
  .back-brand {
    position: absolute; top: 46px; right: 40px;
    display: flex; align-items: center; gap: 12px;
  }
  .brand-mark { width: 18px; height: 18px; background: var(--brand-blue); }
  .brand-name {
    color: var(--text-white); font-weight: 700; font-size: 22px;
    text-transform: uppercase; letter-spacing: 0.5px; line-height: 1.15; text-align: right;
  }
  .contact-block { position: absolute; left: 40px; bottom: 34px; color: var(--text-soft); }
  .person-name {
    color: var(--brand-blue); font-weight: 600; font-size: 20px;
    text-transform: uppercase; letter-spacing: 0.5px; line-height: 1.1;
  }
  .person-role { font-size: 13px; color: var(--text-soft); }
  .divider { width: 170px; height: 2px; background: var(--text-white); margin: 8px 0 10px; }
  .address { font-size: 12px; line-height: 1.45; margin-bottom: 10px; }
  .contact-list { list-style: none; font-size: 12px; line-height: 1.7; }
  .contact-list li { display: flex; align-items: center; gap: 8px; }
  .contact-list svg { width: 12px; height: 12px; flex: none; }
  .abn { margin-top: 8px; color: var(--brand-blue); font-size: 15px; font-weight: 500; }
</style>
</head>
<body>
<main class="canvas">
  <section class="card card-front" aria-label="Card front">
    <div class="front-brand">Ridgeline<br>Building Group</div>
  </section>

  <section class="card card-back" aria-label="Card back">
    <div class="back-brand">
      <span class="brand-mark"></span>
      <div class="brand-name">Ridgeline<br>Building Group</div>
    </div>

    <div class="contact-block">
      <div class="person-name">Liam Carter</div>
      <div class="person-role">CEO/Principal</div>
      <div class="divider"></div>
      <p class="address">42 Harbour View Rd,<br>Eastvale, VIC 3190</p>
      <ul class="contact-list">
        <li>
          <svg viewBox="0 0 12 12"><rect x="3" y="1" width="6" height="10" rx="1" fill="none" stroke="var(--brand-blue)" stroke-width="1.3"/></svg>
          0400 555 218
        </li>
        <li>
          <svg viewBox="0 0 12 12"><rect x="1" y="2.5" width="10" height="7" fill="var(--brand-blue)"/><path d="M1 2.5 6 6.5 11 2.5" fill="none" stroke="var(--card-bg)" stroke-width="1"/></svg>
          info@ridgelinebuilding.com.au
        </li>
        <li>
          <svg viewBox="0 0 12 12"><circle cx="6" cy="6" r="5" fill="var(--brand-blue)"/><path d="M1 6h10M6 1v10" stroke="var(--card-bg)" stroke-width="0.8"/></svg>
          www.ridgelinebuilding.com.au
        </li>
      </ul>
      <div class="abn">ABN: 12 345 678 901</div>
    </div>
  </section>
</main>
</body>
</html>
```